TALRENO Business Cards

We require a business card for our company that provides IT consulting services. We already have a logo that needs to be used on the card. We want a clean professional looking design that incorporates our colours. Our main focus is providing managed services to business, which involves us looking after all of their IT requirements including managing servers/networks, projects, and procurement.

Industry/Entity Type

Information Technology

Requirements
Must have
• our logo, contact information, name, title, phone numbers

```html
<!DOCTYPE html>
<html lang="en">
<head>
<meta charset="UTF-8">
<title>TALRENO Business Cards</title>
<link rel="stylesheet" href="https://fonts.googleapis.com/css2?family=Lato:wght@400;700&display=swap">
<style>
  :root {
    --page: #ffffff;
    --card-dark: #333333;
    --card-light: #fafbfb;
    --brand-blue: #1390c9;
    --text-grey: #555555;
    --text-dark: #3a3a3a;
    --emboss-grey: #8a8a8a;
    --rule-blue: #4aa8d4;
  }
  * { box-sizing: border-box; margin: 0; padding: 0; }
  html, body {
    width: 1200px; height: 1200px; overflow: hidden;
    background: var(--page);
    font-family: "Lato", Arial, sans-serif;
  }
  .canvas { position: relative; width: 1200px; height: 1200px; }

  .card {
    position: absolute; left: 246px; width: 708px; height: 404px;
  }
  .card--front { top: 138px; background: var(--card-dark); }
  .card--back { top: 646px; background: var(--card-light); border: 1px solid #ececec; }

  .wordmark {
    display: flex; align-items: center; font-weight: 700; letter-spacing: 4px;
  }
  .wordmark__dot { border-radius: 50%; flex: none; }

  .card--front .wordmark {
    position: absolute; left: 0; right: 0; top: 0; bottom: 0;
    justify-content: center; gap: 22px;
    color: var(--emboss-grey); font-size: 78px;
  }
  .card--front .wordmark__dot { width: 84px; height: 84px; background: #2a2a2a; }

  .card--back .wordmark {
    position: absolute; left: 48px; top: 84px; gap: 16px;
    color: var(--brand-blue); font-size: 54px;
  }
  .card--back .wordmark__dot { width: 64px; height: 64px; background: var(--brand-blue); }

  .person { position: absolute; right: 48px; top: 236px; text-align: right; }
  .person__name { color: var(--brand-blue); font-size: 28px; font-weight: 700; line-height: 1; }
  .person__title {
    position: absolute; right: 48px; top: 268px;
    color: var(--text-dark); font-size: 17px; font-weight: 700;
  }
  .divider {
    position: absolute; left: 48px; top: 278px; width: 535px; height: 1px;
    background: var(--rule-blue);
  }

  .contacts { position: absolute; left: 48px; top: 298px; list-style: none; }
  .contacts li {
    display: flex; align-items: center; gap: 14px; height: 23.5px;
    color: var(--text-grey); font-size: 16.5px;
  }
  .contacts svg { width: 13px; height: 13px; fill: var(--brand-blue); flex: none; }
  .contacts .accent { color: var(--brand-blue); }

  .address {
    position: absolute; right: 48px; top: 318px; text-align: right;
    color: var(--text-grey); font-size: 16.5px; line-height: 25px; font-style: normal;
  }
</style>
</head>
<body>
<div class="canvas">

  <section class="card card--front" aria-label="Card front">
    <div class="wordmark"><span class="wordmark__dot"></span><span>TALRENO</span></div>
  </section>

  <section class="card card--back" aria-label="Card back">
    <div class="wordmark"><span class="wordmark__dot"></span><span>TALRENO</span></div>

    <div class="person"><p class="person__name">Daniel Arroyo</p></div>
    <div class="divider"></div>
    <p class="person__title">Manager</p>

    <ul class="contacts">
      <li>
        <svg viewBox="0 0 16 16" aria-hidden="true"><path d="M3.6 1.2l2.3 2.5-1.3 1.9c.9 2 2.4 3.5 4.4 4.5l1.9-1.3 2.5 2.3-1.3 2.6C6.5 13.6 2.4 9.5 1.1 3.9z"/></svg>
        <span>+34 910 482 317</span>
      </li>
      <li>
        <svg viewBox="0 0 16 16" aria-hidden="true"><path d="M1 3h14v10H1z M2.5 4.5L8 9l5.5-4.5" fill="var(--brand-blue)" stroke="#fff" stroke-width="1.2"/></svg>
        <span>info@talreno.com</span>
      </li>
      <li>
        <svg viewBox="0 0 16 16" aria-hidden="true"><circle cx="8" cy="8" r="6.5" fill="none" stroke="var(--brand-blue)" stroke-width="1.2"/><ellipse cx="8" cy="8" rx="2.8" ry="6.5" fill="none" stroke="var(--brand-blue)" stroke-width="1"/><path d="M1.5 8h13M2.5 5h11M2.5 11h11" stroke="var(--brand-blue)" stroke-width="1"/></svg>
        <span>www.<span class="accent">talreno</span>.com</span>
      </li>
    </ul>

    <address class="address">Calle del Roble 14<br>Oficina 2B, 28004, Madrid.</address>
  </section>

</div>
</body>
</html>
```